'Our Values' graphic

Hi there,
Could I get few options creating this graphic in a more minimalist, corporate look - using minimalist graphic elements and designs and using minimalist fonts (see google or freepik for inspiration)
I would also like the lines around the outside to be more minimalist. Maybe a thin line or a graphic element.
Change 'Core Values' title to 'Our Values'
Keep the font of 'Values'.
I would like to see a version in all dark grey and another version with the font in the lower square with each line of font being a different colour (Red, Blue, Green and Orange)

Requirements
Must have
• 'Our Values' and using the same font for 'Values' as the original artwork
Nice to have
• Minimalist artwork

```html
<!DOCTYPE html>
<html lang="en">
<head>
<meta charset="utf-8">
<title>Our Values</title>
<link rel="stylesheet" href="https://fonts.googleapis.com/css2?family=Caveat+Brush&family=Poppins:wght@600;800&display=swap">
<style>
  :root {
    --sky: #2a98e6;
    --paper: #ffffff;
    --ink: #595a5c;
    --red: #c8160e;
    --red-edge: #9e0d07;
    --blue: #2773e1;
    --blue-edge: #1b56b0;
    --green: #80bf2c;
    --green-edge: #5e9a17;
    --orange: #ee9700;
    --orange-edge: #c77600;
  }
  * { margin: 0; padding: 0; box-sizing: border-box; }
  html, body { width: 1021px; height: 1200px; overflow: hidden; background: var(--paper); }
  .poster { position: relative; width: 1021px; height: 1200px; background: var(--paper); }
  .frame {
    position: absolute; left: 24px; top: 25px; width: 973px; height: 1150px;
    border: 2px solid var(--sky); border-radius: 40px; overflow: hidden; background: var(--paper);
  }
  .title-band { position: absolute; left: 0; top: 0; width: 100%; height: 558px; background: var(--sky); }
  .title-our {
    position: absolute; left: 404px; top: 88px;
    font-family: "Poppins", sans-serif; font-weight: 600; font-size: 232px;
    line-height: 1; color: var(--paper); letter-spacing: -4px;
  }
  .title-values {
    position: absolute; left: 98px; top: 148px;
    font-family: "Caveat Brush", cursive; font-size: 360px;
    line-height: 1; color: var(--paper); letter-spacing: -6px;
  }
  .value-list { position: absolute; left: 71px; top: 604px; list-style: none; }
  .value { display: flex; align-items: center; height: 100px; margin-bottom: 25px; }
  .value-letter {
    width: 100px; height: 100px; border-radius: 12px;
    display: flex; align-items: center; justify-content: center;
    font-family: "Poppins", sans-serif; font-weight: 800; font-size: 64px; color: var(--paper);
    margin-right: 16px;
  }
  .value-letter.red { background: var(--red); box-shadow: inset -8px -6px 0 var(--red-edge); }
  .value-letter.blue { background: var(--blue); box-shadow: inset -8px -6px 0 var(--blue-edge); }
  .value-letter.green { background: var(--green); box-shadow: inset -8px -6px 0 var(--green-edge); }
  .value-letter.orange { background: var(--orange); box-shadow: inset -8px -6px 0 var(--orange-edge); }
  .value-text {
    font-family: "Poppins", sans-serif; font-weight: 800; font-size: 58px;
    color: var(--ink); letter-spacing: -1.5px; line-height: 1; padding-top: 6px;
  }
</style>
</head>
<body>
<div class="poster">
  <div class="frame">
    <div class="title-band">
      <div class="title-our">OUR</div>
      <div class="title-values">Values</div>
    </div>
    <ul class="value-list">
      <li class="value"><span class="value-letter red">R</span><span class="value-text">ISE TOGETHER</span></li>
      <li class="value"><span class="value-letter blue">I</span><span class="value-text">NNOVATE EDUCATION</span></li>
      <li class="value"><span class="value-letter green">S</span><span class="value-text">AFETY FIRST</span></li>
      <li class="value"><span class="value-letter orange">E</span><span class="value-text">MPOWER CONNECTIONS</span></li>
    </ul>
  </div>
</div>
</body>
</html>
```